Talvin Foundation Letterhead

We are a newly established non profit registered in Maryland but operates in Africa, south of the sahara. We offer scholarships to deserving young adults from high school through college. Our color theme for our existing logo is purple, we want a design that is stylish, spellbinding yet a letterhead that projects seriousness. More information on www.thetalvinfoundation.example

Target Market(s)

High school and college students in sub saharan African as well as our donors in the US

Industry/Entity Type

Non Profit

Font styles to use
Script

Requirements
Must have
• Logo at the top and if possible watermark the logo in the middle of the letterhead, contact address,
Should not have
• NA

```html
<!DOCTYPE html>
<html lang="en">
<head>
<meta charset="utf-8">
<title>Talvin Foundation Letterhead</title>
<link rel="stylesheet" href="https://fonts.googleapis.com/css2?family=Cabin:wght@500&display=swap">
<style>
  :root {
    --purple: #6e3f8a;
    --purple-dark: #4f1f63;
    --mark-grey: #e6e4ec;
    --mark-lilac: #d9cde4;
    --paper: #ffffff;
    --backdrop: #ececef;
    --footer-text: #ffffff;
  }
  * { margin: 0; padding: 0; box-sizing: border-box; }
  html, body {
    width: 1200px; height: 1000px; overflow: hidden;
    background: var(--backdrop);
  }
  .letterhead {
    position: absolute; left: 250px; top: 48px;
    width: 700px; height: 905px;
    background: var(--paper);
    overflow: hidden;
  }
  .brand-header {
    position: absolute; left: 158px; top: 30px;
    display: flex; align-items: center; gap: 16px;
  }
  .brand-circle {
    width: 64px; height: 64px; border-radius: 50%;
    border: 4px solid var(--mark-grey);
  }
  .brand-name {
    font-family: "Cabin", sans-serif; font-weight: 500;
    font-size: 26px; line-height: 1; color: var(--purple);
    white-space: nowrap;
  }
  .watermark {
    position: absolute; left: 235px; top: 364px;
    width: 220px; height: 220px; border-radius: 50%;
    border: 10px solid var(--mark-grey);
    display: flex; align-items: center; justify-content: center;
  }
  .watermark-name {
    font-family: "Cabin", sans-serif; font-weight: 500;
    font-size: 24px; line-height: 1.2;
    color: var(--mark-lilac); text-align: center;
  }
  .footer-curves { position: absolute; left: 0; top: 735px; }
  .footer-contact {
    position: absolute; left: 0; top: 862px; width: 700px;
    font-family: "Cabin", sans-serif; font-weight: 500; font-size: 11px;
    color: var(--footer-text);
  }
  .footer-address {
    position: absolute; right: 362px; top: 3px; text-align: center;
    line-height: 14px; white-space: nowrap;
  }
  .footer-divider {
    position: absolute; left: 417px; top: 0; width: 1px; height: 34px;
    background: var(--footer-text);
  }
  .footer-lines { position: absolute; left: 427px; top: 2px; font-size: 10.5px; }
  .footer-line { display: flex; align-items: center; gap: 5px; height: 17px; }
  .footer-line svg { width: 10px; height: 10px; }
</style>
</head>
<body>
<main class="letterhead">
  <header class="brand-header">
    <div class="brand-circle"></div>
    <div class="brand-name">Talvin Foundation Inc</div>
  </header>

  <div class="watermark">
    <div class="watermark-name">Talvin<br>Foundation</div>
  </div>

  <svg class="footer-curves" width="700" height="170" viewBox="0 0 700 170" aria-hidden="true">
    <defs>
      <linearGradient id="bandFill" x1="0" y1="0" x2="1" y2="0">
        <stop offset="0" stop-color="#7a4690"/>
        <stop offset="0.6" stop-color="#8a62a4"/>
        <stop offset="1" stop-color="#5e2d75"/>
      </linearGradient>
    </defs>
    <path d="M0,79 Q330,100 622,22 Q380,88 0,103 Z" fill="var(--purple-dark)"/>
    <path d="M0,112 Q400,112 700,6 L700,170 L0,170 Z" fill="url(#bandFill)"/>
  </svg>

  <footer class="footer-contact">
    <p class="footer-address">Unit 4, 210 Harbor Lane, Baltimore,<br>MD, USA</p>
    <div class="footer-divider"></div>
    <div class="footer-lines">
      <p class="footer-line">
        <svg viewBox="0 0 10 10"><rect x="0.5" y="1.5" width="9" height="7" fill="none" stroke="#fff"/><path d="M0.5,1.5 L5,5.5 L9.5,1.5" fill="none" stroke="#fff"/></svg>
        hello@talvinfoundation.example
      </p>
      <p class="footer-line">
        <svg viewBox="0 0 10 10"><path d="M2,0.5 L4,2.5 L3,4 Q4.5,6.5 6,7 L7.5,6 L9.5,8 L8,9.5 Q3,9 0.5,2 Z" fill="#fff"/></svg>
        0410-555-0187
      </p>
    </div>
  </footer>
</main>
</body>
</html>
```